Poster Redesign: Layered Core Methods Seminar

Specifically, we need a new poster for an upcoming course we are teaching on the topic of visceral manipulation / bodywork for the abdomen.

The posters / fliers we use to advertise upcoming continuing education workshops in bodywork and acupuncture need a facelift! Colors tend to be cobalt blue, greys, plenty of white space. Brand should communicate both sophistication, elegance and also the warmth and approachability to hands-on therapies like bodywork. It would be great to include some type of hand-wrought element in the illustration: colored pencil, graphite. Our website is www.quietharborcollege.com. Check out the meaning / origin of the name Quiet Harbor College on our facebook page. Fonts are: Proxima Nova. LTC Bodini 175 for italicized quotes. All text is included in existing poster design.

Target Market(s)

acupuncturists, manual therapists / bodyworkers, physical therapists, students in massage therapy school, students in naturopathic medical school

Industry/Entity Type

Health And Wellness

Font styles to use
Sans Serif

Colors
0555a3
d3d3d3
ffffff
85abd2
eaf1f7

Requirements
Must have
• All the text that is provided on the sample draft PDF (attached) must be included.
• Other must haves:
• -Clarity: Clean lines. Lack of clutter.
• -8.5 x 11 or other standard size preferred
Nice to have
• High quality hand-wrought illustration details or effects. would prefer grey scale in this area. Cannot be cartoonish.
Should not have
• Kitchy / pre-formed clip-art style features or tacky cartoony graphics will not be allowed.

```html
<!DOCTYPE html>
<html lang="en">
<head>
<meta charset="utf-8">
<title>Layered Core Methods Seminar</title>
<link href="https://fonts.googleapis.com/css2?family=Open+Sans:wght@300;400&family=Source+Sans+3:wght@400;700&family=Arimo:wght@400&display=swap" rel="stylesheet">
<style>
  :root {
    --frame-blue: #48579a;
    --ink-blue: #3d4d93;
    --paper: #ffffff;
    --text: #1c1c1c;
    --mist: #d3d9e6;
    --slate: #7a87a8;
  }
  html, body { margin: 0; padding: 0; overflow: hidden; }
  body { width: 849px; height: 1200px; background: var(--frame-blue); position: relative; }
  .poster { position: absolute; inset: 0; width: 849px; height: 1200px; overflow: hidden; background: var(--frame-blue); }
  .sheet { position: absolute; left: 34px; top: 28px; width: 784px; height: 920px; background: var(--paper); overflow: hidden; }
  .hero-photo { position: absolute; left: 318px; top: 0; width: 466px; height: 356px; }
  .brand { position: absolute; left: 16px; top: 104px; display: flex; align-items: center; gap: 10px;
    font-family: "Open Sans", sans-serif; font-weight: 400; font-size: 22px; color: var(--ink-blue); }
  .brand-dot { width: 14px; height: 14px; border-radius: 50%; background: var(--ink-blue); }
  .course-title { position: absolute; left: 19px; top: 204px; margin: 0;
    font-family: "Open Sans", sans-serif; font-weight: 300; font-size: 54px; line-height: 53px; color: var(--ink-blue); letter-spacing: 0; }
  .instructor { position: absolute; left: 24px; top: 354px; margin: 0; white-space: nowrap;
    font-family: "Open Sans", sans-serif; font-weight: 300; font-size: 37px; color: var(--ink-blue); }
  .instructor .with { font-size: 22px; }
  .instructor sup { font-size: 16px; vertical-align: 20px; }
  .content { position: absolute; left: 24px; top: 402px; width: 742px;
    font-family: "Source Sans 3", sans-serif; font-size: 16px; line-height: 18px; color: var(--text); }
  .content p { margin: 0 0 18px; }
  .content b { font-weight: 700; }
  .details { position: absolute; top: 964px; font-family: "Arimo", sans-serif; color: #fff; }
  .when-where { left: 34px; font-size: 19px; line-height: 25px; letter-spacing: 0.5px; }
  .when-where p, .pricing p, .schedule p { margin: 0 0 25px; }
  .pricing { left: 417px; width: 200px; font-size: 14.5px; line-height: 19.5px; letter-spacing: 0.6px; }
  .pricing p { margin-bottom: 19px; }
  .schedule { left: 648px; font-size: 14.5px; line-height: 19.5px; letter-spacing: 0.2px; }
  .schedule p { margin-bottom: 19px; }
</style>
</head>
<body>
<div class="poster">
  <div class="sheet">
    <svg class="hero-photo" role="img" aria-label="Photograph of a practitioner's hands applying gentle pressure to a client's abdomen, softly vignetted in blue-grey tones" viewBox="0 0 466 356">
      <defs>
        <radialGradient id="heroTone" cx="0.52" cy="0.45" r="0.55">
          <stop offset="0" stop-color="#6d7fa6"/>
          <stop offset="0.45" stop-color="#9fb0cf"/>
          <stop offset="0.8" stop-color="#dde5f1"/>
          <stop offset="1" stop-color="#ffffff"/>
        </radialGradient>
      </defs>
      <rect width="466" height="356" fill="#fff"/>
      <ellipse cx="248" cy="160" rx="240" ry="220" fill="url(#heroTone)"/>
    </svg>

    <div class="brand"><span class="brand-dot"></span><span>Quiet Harbor College</span></div>

    <h1 class="course-title">LAYERED<br>CORE<br>METHODS</h1>
    <p class="instructor"><span class="with">WITH</span> DANIEL ASHWORTH, LAc, LMT<sup>#20817</sup></p>

    <div class="content">
      <p><b>ABOUT THIS COURSE:</b>The abdomen is a rich area for treatment of all types of symptom pictures. In our experience, the abdomen responds incredibly well to an approach that combines visceral manipulation techniques with acupuncture. This course offers a unique opportunity for people to learn an approach that seamlessly combines visceral manipulation techniques with acupuncture. One of the benefits of putting the abdomen in your hands as a practitioner is that you open the gates for improved diagnostic understanding and improved treatment results.</p>
      <p>Visceral manipulation is essentially myofascial release applied to the viscera. In the class we will spend some time mapping the abdomen anatomically, overlaying our channel and point understanding with the location of the different organs and other structures. As we better understand the nature and location of the abdominal structures we will explore applying myofascial-visceral techniques to specifc structures. This class will be one of a series on the abdomen and will focus on the upper abdomen. For more info: www.quietharborcollege.com</p>
      <p><b>DANIEL ASHWORTH</b>, LAc, LMT is adjunct faculty at WCIM and has a thriving practice in Portland. Daniel has been fortunate to have trained closely with luminary figures in bodywork and cranialsacral felds. He is happy to share what he has learned from integrating Chinese medicine with his 16 years of experience in cranialsacral, myofascial release, visceral manipulation, and active isolated stretching techniques.</p>
      <p><b>CONTINUING EDUCATION:</b> NBAOM &amp; OBAT CE hours available pending approval</p>
      <p><b>PREREQUISITES:</b> Participants must be licensed, certifed health professionals or enrolled in an accredited healthcare program or otherwise legally entitled to practice hands-on therapy.</p>
      <p><b>REGISTER:</b> We hope you will join us! To receive more information or to reserve your spot, register online at www.quietharborcollege.com.</p>
    </div>
  </div>

  <div class="details when-where">
    <p>DATE &amp; TIME:<br>SAT, OCT 7th<br>9:30 AM - 5:30 PM</p>
    <p>LOCATION:<br>Lotus Hall Studio<br>2480 NE Alder Ave.<br>Suite #118<br>Portland, OR 97214</p>
  </div>

  <div class="details pricing">
    <p>COST: $225.00<br>Full-time students in an accredited healthcare program may register at a discounted rate of $200.</p>
    <p>2017/2018 TRAININGS:<br>CS1: OCT 21-22, 2017<br>CS2: NOV 11-12, 2017<br>CS3: APRIL 28, 2018</p>
  </div>

  <div class="details schedule">
    <p>ACTIVE ISOLATED<br>STRETCHING:<br>AIS I: SEP 23, 2017<br>AIS II: JUNE 9, 2018</p>
    <p>MFR1: FEB 3-4, 2018<br>MFR2: NOV 4 - 5, 2017<br>MFR3: JUNE 2-3, 2018</p>
    <p>SKILLS SESSIONS:<br>LOW BACK: JULY 18<br>DIAPHRAGM: AUG 8</p>
  </div>
</div>
</body>
</html>
```